Vintrel.com- International Goal Achievement Coach Needs Website Design

I need a web design for my new company called Vintrel. I help people who are stuck, people who have a big dream, but don't know how to get there. I help them to break their dreams down into small, manageable steps... and then I'm the "kick in the shin" to get them moving and thriving!

We can all be better- We can all DO better. I inspire people to Ride Onward in the direction of your dreams.

I have uploaded my logo along with some vintage champagne posters. Please use the vintage posters as inspiration. I like the bold, vintage look and feel. I would love the main colors of the design to be black, white and metallic gold. And to follow along this vintage look and feel. Please feel free to use the logo in black or metallic gold or white.

Target Market(s)

websites that I like- janetrulsby.com & hollyp.tv

I would like to also use the vintage champagne photos attached as inspiration as well.

Industry/Entity Type

It Company

Requirements
Must have
• Tabs should include: About, Work With Me, Praise, Giving Back

On the homepage add:
* Sign up for newsletter with space to enter name and email (No click throughs)
* Upcoming Events/Sessions
* Newsletter Posts
* Resources
* Praise Section

* Large photo on top with additional photos throughout the page/site.
Nice to have
• Any additions you can bring to the table would be greatly appreciated.

```html
<!DOCTYPE html>
<html lang="en">
<head>
<meta charset="utf-8">
<title>Vintrel – Goal Achievement Coaching</title>
<link rel="stylesheet" href="https://fonts.googleapis.com/css2?family=Source+Sans+3:wght@400;600&family=Arimo:wght@400;700&display=swap">
<style>
:root{
  --gold:#a97447;
  --gold-dark:#8b5a31;
  --gold-light:#d49a60;
  --ink:#2a2a2a;
  --text:#3a3a3a;
  --dark:#1b1b1b;
  --darker:#111;
  --line:#d9d9d9;
  --white:#fff;
}
*{box-sizing:border-box;margin:0;padding:0}
html,body{width:754px;height:1200px;overflow:hidden;background:var(--white)}
body{position:relative;font-family:"Arimo",Arial,sans-serif;color:var(--text)}
.abs{position:absolute}
.top-rule{left:0;top:0;width:754px;height:5px;background:#3a3a3a}

/* header */
.brand{left:97px;top:12px;display:flex;align-items:center;gap:14px}
.brand-mark{width:66px;height:66px;border-radius:50%;background:var(--gold)}
.brand-name{font-family:"Source Sans 3",sans-serif;font-size:34px;font-weight:400;color:var(--gold);border-left:1px solid var(--gold);padding-left:14px;line-height:56px}
.search{left:470px;top:18px;width:187px;height:21px;border:2px solid var(--gold);border-radius:11px;font-size:9px;color:#999;padding:3px 8px}
.search svg{position:absolute;right:4px;top:2px}
.social{left:516px;top:54px;display:flex;align-items:center;gap:4px;font-size:10px;color:#333}
.social span.label{margin-right:4px}
.social i{display:block;width:18px;height:18px;background:var(--gold)}

/* nav */
.nav{left:0;top:86px;width:754px;height:28px;background:linear-gradient(#c08755,#8d5a30)}
.nav ul{list-style:none;position:absolute;left:98px;top:0;display:flex;height:28px}
.nav li{font-size:10px;color:var(--white);line-height:28px;text-align:center;border-right:1px solid rgba(0,0,0,.18)}
.nav li.active{background:#2a2a2a}

/* hero */
.hero{left:0;top:114px;width:754px;height:277px;background:linear-gradient(100deg,#d9d7d3 0%,#c7c3be 35%,#8f2a2a 45%,#b73333 55%,#cfcac4 70%,#a7a29b 100%)}
.hero-shade{left:0;top:270px;width:754px;height:121px;background:linear-gradient(rgba(0,0,0,0),rgba(0,0,0,.55) 35%,rgba(0,0,0,.8))}
.hero-caption{left:98px;top:306px;width:300px;color:var(--white)}
.hero-caption h2{font-family:"Source Sans 3",sans-serif;font-weight:400;font-size:16px;color:var(--gold-light);margin-bottom:6px}
.hero-caption p{font-size:9.5px;line-height:15px}
.signup{left:411px;top:215px;width:244px;height:160px;background:rgba(20,20,20,.6);border:1px solid rgba(255,255,255,.35);border-radius:3px;padding:12px 13px}
.signup p{font-size:11px;line-height:18px;color:var(--white);margin-bottom:8px}
.signup .field{height:19px;border:2px solid var(--gold);border-radius:3px;background:var(--white);font-size:8.5px;color:#555;padding:2px 5px;margin-bottom:7px}
.signup .submit{width:68px;height:22px;background:var(--gold);border:1px solid #e0b58a;border-radius:3px;color:var(--white);font-size:11px;text-align:center;line-height:20px;margin-top:4px}
.arrow{width:27px;height:27px;border-radius:50%;background:#111;border:2px solid #ddd;top:240px}

/* content */
.main{left:98px;top:405px;width:355px}
.sidebar{left:461px;top:391px;width:194px;height:629px;border-left:1px solid var(--line);border-right:3px solid #e3e3e3}
h3.title{font-family:"Source Sans 3",sans-serif;font-weight:400;font-size:18px;color:#222}
h3.title em,h4.side-title em{font-style:normal;color:var(--gold)}
.post p{font-size:8.4px;line-height:13.3px;text-align:justify;margin-top:8px}
.post p + p{margin-top:10px}
.actions{display:flex;gap:5px;margin-top:9px}
.btn{height:19px;font-size:9px;line-height:19px;padding:0 7px;color:var(--white);border-radius:2px}
.btn.more{background:var(--gold)}
.btn.count{background:#111}
.divider{height:1px;background:var(--line);margin:18px 0 14px}
.player{margin:17px 0 0 33px;width:297px;height:185px;background:#ddd;border-radius:6px;padding:6px 8px 22px;box-shadow:0 4px 5px rgba(0,0,0,.15)}
.player .screen{height:100%;background:#0c0c0c;position:relative}
.player .frame{position:absolute;left:36px;right:36px;top:0;bottom:10px;background:#1e5166}
.player .bar{position:absolute;left:0;right:0;bottom:0;height:10px;background:#222}
.play{position:absolute;left:50%;top:50%;width:18px;height:18px;margin:-9px 0 0 -9px;border-radius:50%;background:rgba(255,255,255,.18);border:1px solid rgba(255,255,255,.6)}
.play::after{content:"";position:absolute;left:6px;top:4px;border-left:6px solid #fff;border-top:4px solid transparent;border-bottom:4px solid transparent}

h4.side-title{font-family:"Source Sans 3",sans-serif;font-weight:400;font-size:13px;color:#222;position:absolute;left:9px}
.side-box{position:absolute;left:8px;width:179px;border:4px solid #ddd;background:#ddd}
.side-video{top:46px;height:110px}
.side-video .screen{height:100%;background:#0c0c0c;position:relative}
.side-video .frame{position:absolute;left:14px;right:14px;top:0;bottom:8px;background:#5a2e1d}
.posters{position:absolute;left:12px;top:202px;display:flex;gap:6px}
.poster{width:50px;height:73px;border:2px solid #ddd}
.side-photo{top:320px;height:111px;background:linear-gradient(#6aa6da,#bcd8ee 55%,#c79d3d 75%,#6d8f45)}
.quote{position:absolute;left:8px;top:477px;width:179px;height:122px;border:1px solid var(--line);padding:13px 9px;font-size:7.8px;line-height:12.5px;text-align:justify;color:#222}
.quote .by{display:block;text-align:right;color:var(--gold-dark);font-weight:700;margin-top:6px}
.quote .ctrl{position:absolute;right:10px;bottom:6px;font-size:11px;color:#666}

/* footer */
.footer{left:0;top:1020px;width:754px;height:156px;background:var(--dark);border-top:3px solid var(--gold)}
.footer h5{position:absolute;top:15px;font-family:"Source Sans 3",sans-serif;font-weight:400;font-size:15px;color:var(--white)}
.footer h5 em{font-style:normal;color:var(--gold)}
.links{position:absolute;left:98px;top:48px;display:flex;gap:39px}
.links ul{list-style:none}
.links li{font-size:7.5px;color:#ddd;line-height:19.5px;font-weight:700}
.nl-text{position:absolute;left:318px;top:46px;width:190px;font-size:7.5px;line-height:13px;color:#ddd;font-weight:700}
.nl-form{position:absolute;left:317px;top:83px;width:161px;height:17px;background:#4a4a4a;border-radius:3px}
.nl-form .join{position:absolute;right:2px;top:2px;height:13px;width:41px;background:var(--gold);border-radius:2px;font-size:7px;font-weight:700;color:var(--white);text-align:center;line-height:13px}
.emblem{position:absolute;left:572px;top:45px;width:66px;height:66px;border-radius:50%;background:#888;border:4px solid #bbb}
.legal{left:0;top:1176px;width:754px;height:24px;background:var(--darker);font-size:7px;color:#aaa;text-align:center;line-height:24px}
</style>
</head>
<body>
<div class="abs top-rule"></div>

<header>
  <div class="abs brand"><span class="brand-mark"></span><span class="brand-name">Vintrel</span></div>
  <div class="abs search">Search_
    <svg width="14" height="14" viewBox="0 0 14 14"><circle cx="7" cy="7" r="6" fill="none" stroke="#8b5a31" stroke-width="1.3"/><circle cx="6.5" cy="6.5" r="2.6" fill="none" stroke="#8b5a31" stroke-width="1.2"/><line x1="8.3" y1="8.3" x2="10.5" y2="10.5" stroke="#8b5a31" stroke-width="1.3"/></svg>
  </div>
  <div class="abs social"><span class="label">Get Social:</span><i></i><i></i><i></i><i></i></div>
</header>

<nav class="abs nav">
  <ul>
    <li class="active" style="width:50px">Home</li>
    <li style="width:63px">About Us</li>
    <li style="width:81px">Work with me</li>
    <li style="width:50px">Praise</li>
    <li style="width:50px">Books</li>
    <li style="width:51px">Events</li>
    <li style="width:46px">Press</li>
    <li style="width:72px">Giving Back</li>
    <li style="width:74px;border-right:0">Contact  us</li>
  </ul>
</nav>

<section class="hero-block">
  <div class="abs hero" role="img" aria-label="Joyful woman in a red sweater raising her arms in a bright kitchen"></div>
  <div class="abs hero-shade"></div>
  <div class="abs arrow" style="left:1px"><svg width="23" height="23" viewBox="0 0 23 23"><polyline points="13,6 8,11.5 13,17" fill="none" stroke="#fff" stroke-width="2"/></svg></div>
  <div class="abs arrow" style="left:725px"><svg width="23" height="23" viewBox="0 0 23 23"><polyline points="10,6 15,11.5 10,17" fill="none" stroke="#fff" stroke-width="2"/></svg></div>
  <div class="abs hero-caption">
    <h2>Consectetuer adipiscing elit</h2>
    <p>Sed diam nonummy nibh euismod tincidunt ut laoreet dolore magna aliquam erat volutpat. Ut wisi enim ad minim veniam, quis nostrud exerci tation ullamcorper suscipit lobortis.</p>
  </div>
  <form class="abs signup">
    <p>Lorem ipsum dolor sit amet, consectass etuer adipiscing elit, sed diam nonummy.</p>
    <div class="field">Your name_</div>
    <div class="field">Your email_</div>
    <div class="submit">SUBMIT</div>
  </form>
</section>

<main class="abs main">
  <article class="post">
    <h3 class="title">Consectetuer <em>Adipiscing elit</em></h3>
    <p>Lorem ipsum dolor sit amet, consectetuer adipiscing elit, sed diam nonummy nibh euismod tincidunt ut laoreet dolore magna aliquam erat volutpat. Ut wisi enim ad minim veniam, quis nostrud exerci tation ullamcorper suscipit lobortis nisl ut aliquip ex ea commodo consequat. Duis autem vel eum iriure dolor in hendrerit in vulputate velit esse molestie consequat, vel illum dolore eu feugiat nulla facilisis at vero eros et accumsan et iusto odio dignissim qui blandit praesent luptatum zzril delenit augue duis dolore te feugait nulla facilisi.</p>
    <p>Ut wisi enim ad minim veniam, quis nostrud exerci tation ullamcorper suscipit lobortis nisl ut aliquip ex ea commodo consequat. Duis autem vel eum iriure dolor in hendrerit in vulputate velit esse molestie consequat, vel illum dolore eu feugiat nulla facilisis at vero eros et accumsan et iusto odio dignissim qui blandit praesent luptatum zzril delenit augue duis dolore te feugait nulla facilisi. Lorem ipsum dolor sit amet, consectetuer adipiscing elit, sed diam nonummy nibh euismod tincidunt ut laoreet dolore magna aliquam erat volutpat.</p>
    <div class="actions"><span class="btn more">READ MORE</span><span class="btn count">20 COMMENTS</span></div>
  </article>
  <div class="divider"></div>
  <article class="post">
    <h3 class="title">Hendrerit in vulputater <em>Adipiscing elit</em></h3>
    <p>Lorem ipsum dolor sit amet, consectetuer adipiscing elit, sed diam nonummy nibh euismod tincidunt ut laoreet dolore magna aliquam erat volutpat. Ut wisi enim ad minim veniam, quis nostrud exerci tation ullamcorper suscipit lobortis nisl.</p>
    <div class="player"><div class="screen"><div class="frame" role="img" aria-label="Video still"></div><span class="play"></span><div class="bar"></div></div></div>
    <div class="actions" style="margin-top:20px"><span class="btn more">READ MORE</span><span class="btn count">20 COMMENTS</span></div>
  </article>
</main>

<aside class="abs sidebar">
  <h4 class="side-title" style="top:19px">Consectetuer <em>Adipiscing elit</em></h4>
  <div class="side-box side-video"><div class="screen"><div class="frame" role="img" aria-label="Video still"></div><span class="play"></span></div></div>
  <h4 class="side-title" style="top:176px">Nonummy  <em>Molestie</em></h4>
  <div class="posters">
    <div class="poster" role="img" aria-label="Vintage champagne poster" style="background:linear-gradient(#d8c79a,#b9853e)"></div>
    <div class="poster" role="img" aria-label="Vintage champagne poster" style="background:linear-gradient(#e9b33a,#2c2a28)"></div>
    <div class="poster" role="img" aria-label="Vintage champagne poster" style="background:linear-gradient(#f3e3b5,#c9962e)"></div>
  </div>
  <h4 class="side-title" style="top:294px">Consectetuer <em>Adipiscing elit</em></h4>
  <div class="side-box side-photo" role="img" aria-label="Two people leaping joyfully in front of a yellow house"></div>
  <h4 class="side-title" style="top:451px">Consectetuer <em>Adipiscing elit</em></h4>
  <blockquote class="quote">“Lorem ipsum dolor sit amet, consectetuer adipiscing elit, sed diam nonummy nibh euismod tincidunt ut laoreet dolore magna aliquam erat volutpat. Ut wisi enim ad minim veniam, quis nostrud exerc.”
    <span class="by">-Exercitation Ullamcorpe</span>
    <span class="ctrl"><span style="color:var(--gold)">&#8249;</span> &#8250;</span>
  </blockquote>
</aside>

<footer class="abs footer">
  <h5 style="left:98px"><em>MAIN</em> LINKS</h5>
  <div class="links">
    <ul><li>Home</li><li>About Us</li><li>Work with me</li><li>Praise</li><li>Books</li></ul>
    <ul><li>Events</li><li>Press</li><li>Giving Back</li><li>Contact  us</li></ul>
  </div>
  <h5 style="left:318px"><em>NEWSLETTER</em> SIGNUP</h5>
  <p class="nl-text">Lorem ipsum dolor sit amet, consectetuer Ads adipiscing elit, sed diam nonummy nibh</p>
  <div class="nl-form"><span class="join">JOIN US</span></div>
  <div class="emblem"></div>
</footer>
<div class="abs legal">Privacy Policy &nbsp;|&nbsp; © 2014 Vintrel &nbsp;|&nbsp; Terms Policy &nbsp;|&nbsp; Disclaimer</div>
</body>
</html>
```